KQR Silver Moon Party

Hi
Need to design Party Invitation. Needs to be very glamourous/nightclub party scene. Very classy but funky.

I've attached two files:

one is a mock up of the invitation that I need, except the date is now changed to Saturday 10th August.

Also, I have attached an example of an All Black party invitation that I found that I like the look of.

Thanks

Target Market(s)

20's to 40's party people

Requirements
Must have
• Must have a glamorous, sexy black (and bling) theme.

My logo. attached.

```html
<!DOCTYPE html>
<html lang="en">
<head>
<meta charset="utf-8">
<title>KQR Silver Moon Party – Invitation</title>
<link rel="stylesheet" href="https://fonts.googleapis.com/css2?family=Alfa+Slab+One&family=Great+Vibes&family=Josefin+Sans:wght@600;700&display=swap">
<style>
  :root {
    --page: #ffffff;
    --card: #0a0a0a;
    --ink: #f4f4f4;
    --accent: #a3246f;
    --pattern-dark: #151515;
    --pattern-light: #3a3a3a;
    --silver-dark: #2a2a2a;
    --silver-light: #f2f2f2;
  }
  * { margin: 0; padding: 0; box-sizing: border-box; }
  html, body {
    width: 1200px;
    height: 1000px;
    overflow: hidden;
    background: var(--page);
  }
  .invitation {
    position: absolute;
    left: 270px;
    top: 40px;
    width: 660px;
    height: 920px;
    background: var(--card);
    color: var(--ink);
    text-align: center;
    overflow: hidden;
  }
  .lattice {
    position: absolute;
    left: 0;
    width: 100%;
    background: linear-gradient(180deg, var(--pattern-dark), var(--pattern-light) 50%, var(--pattern-dark));
  }
  .lattice--top { top: 0; height: 100px; }
  .lattice--bottom { top: 752px; height: 168px; }
  .silver-band {
    position: absolute;
    left: 0;
    width: 100%;
    height: 12px;
    background: linear-gradient(90deg, var(--silver-dark), var(--silver-light) 45%, #bdbdbd 60%, var(--silver-dark));
  }
  .silver-band--top { top: 96px; }
  .silver-band--bottom { top: 744px; }
  .block { position: absolute; left: 0; width: 100%; }
  .script {
    font-family: "Great Vibes", cursive;
    font-weight: 400;
  }
  .caps {
    font-family: "Josefin Sans", sans-serif;
    font-weight: 700;
    text-transform: uppercase;
    letter-spacing: 0.08em;
  }
  .invite-line { top: 160px; font-size: 34px; }
  .event-title {
    top: 222px;
    font-family: "Alfa Slab One", serif;
    font-size: 31px;
    line-height: 1.05;
    letter-spacing: 0.02em;
    text-transform: uppercase;
  }
  .event-date { top: 312px; font-size: 18px; }
  .event-time { top: 342px; font-size: 12px; }
  .event-venue { top: 390px; font-size: 16px; }
  .sep { color: var(--accent); margin: 0 14px; }
  .tickets-heading { top: 442px; font-size: 32px; }
  .ticket-prices { top: 488px; font-size: 15px; }
  .ticket-outlets { top: 534px; font-size: 12px; line-height: 1.45; }
  .inclusions { top: 604px; font-size: 22px; line-height: 1.2; }
  .inclusions .dots { color: var(--accent); font-family: "Josefin Sans", sans-serif; font-size: 10px; letter-spacing: 0.3em; display: block; margin: 2px 0 0; }
  .entry-conditions { top: 716px; font-size: 9px; line-height: 1.5; }
  .brand {
    top: 800px;
    display: flex;
    justify-content: center;
    align-items: center;
    gap: 10px;
  }
  .brand-mark {
    width: 12px;
    height: 12px;
    border-radius: 50%;
    background: var(--accent);
  }
  .brand-name {
    font-family: "Josefin Sans", sans-serif;
    font-weight: 700;
    font-size: 18px;
    letter-spacing: 0.08em;
    text-transform: uppercase;
    color: var(--accent);
  }
</style>
</head>
<body>
  <main class="invitation">
    <div class="lattice lattice--top" role="img" aria-label="Decorative diamond lattice pattern with small silver flowers"></div>
    <div class="silver-band silver-band--top"></div>

    <p class="block script invite-line">You are cordially invited to the</p>
    <h1 class="block event-title">KQR<br>Silver Moon Winter Party</h1>

    <p class="block caps event-date">Saturday, August 10</p>
    <p class="block caps event-time">8pm till late</p>
    <p class="block caps event-venue">Harbour Lodge<span class="sep">✦</span>The Vault Bar<span class="sep">✦</span>Coral Bay</p>

    <h2 class="block script tickets-heading">Tickets</h2>
    <p class="block caps ticket-prices">$40 KQR Clients<span class="sep">✦</span>$50 Public</p>
    <p class="block caps ticket-outlets">From Harbour Lodge (02) 5550 1234<br>or KQR 0400 555 012</p>

    <p class="block script inclusions">Flowing champagne, wine beer and canapes included<span class="dots">✦✦✦</span>DJ Velvet Keys Spinning tunes</p>

    <p class="block caps entry-conditions">Conditions of entry<br>Entry only if you are over 18 and you have on all black</p>

    <div class="silver-band silver-band--bottom"></div>
    <div class="lattice lattice--bottom" role="img" aria-label="Decorative diamond lattice pattern with small silver flowers"></div>

    <div class="block brand">
      <span class="brand-mark"></span>
      <span class="brand-name">KQR Personal Training</span>
    </div>
  </main>
</body>
</html>
```